Wine Label Logo NEW name too

We would like to see this done in more colors but, lighter ones too. the dark colors don't show up that well. Can you also do some on white wine and not just red wine?

Also, we aren't sure we will use the name Plumvelle and wonder if you could use the name Nutmeadow with the same design to see how that looks, as well?

new wine label for a brand called Plumvelle (one word) and is targeted to go after 21-40 year olds. Probably more women than men. There will be Plumvelle Red, Plumvelle White, Plumvelle Cabernet, etc. the profile of the wine will be sweet...duh!!

would love you to come up with some TAG LINE ideas, as well. Size should be between 2 1/2 to 3 inches wide and 5 to 6 inches long. Needs place holders for varietal, Cabernet. 13.5% alcohol, area wil be California. I suggest you look at a bunch of wine labels to better understand this brief.

The final design should communicate fun, sweet, wine, young, hip

Wine labels matter. Period. Now, attempting to define “fun and contemporary” is nigh on impossible, but I think it would be safe to assume that this could mean “non-traditional.” Let’s face it. Design matters to millennial consumers. Quill, Tern Lodges, Hearthline Magazine – these brands are not ONLY for millennials by any means (well, maybe Tern), but design is top priority for these brands, and these brands have top priority for millennials. Feel free to do the math. If we spend money on something, we expect it to be beautiful and often times we expect social purchases like wine to act as a public reflection of our tastes and personality. This latter expectation is no different than any other generation (if arguably more intense due to our intrinsic personal branding tendencies); however, our personalities and what we are reflecting out to our peers IS different.
Updates

What about a label that is 2 1/2 to 3 inches wide and 5-6 inches long and looks like a white or off white piece of paper that has had berries poured across it with some stains and the name Plumvelle Cabernet as the logo on the label?  Needs space for the AVA area grown to say California and the vintage 2011 and alcohol level in small letters 12.3%. 

Look at some wine labels to get a unique idea. Needs to appeal to 21-40 year old women. Needs to denote the wine is sweet

Reason: two partners are out of the country and I want them involved in the choice

Target Market(s)

Industry/Entity Type

Social

Logo Text

Plumvelle Cabernet

Logo styles of interest
Pictorial/Combination Logo
Abstract Logo
Wordmark Logo

```html
<!DOCTYPE html>
<html lang="en">
<head>
<meta charset="utf-8">
<title>Nutmeadow and Plumvelle wine labels</title>
<link rel="stylesheet" href="https://fonts.googleapis.com/css2?family=Parisienne&family=Sorts+Mill+Goudy:ital@0;1&family=Uncial+Antiqua&family=Source+Sans+3:wght@400&display=swap">
<style>
  :root {
    --paper: #ffffff;
    --ink: #111111;
    --wine-bright: #cc2240;
    --wine-deep: #8c0e1f;
    --wine-edge: #5a0610;
    --gold: #e3c87a;
    --cream: #f6e4bf;
    --blush: #f2d3c6;
    --rim: #e27a8a;
    --emblem: #9c1328;
    --text-dark: #2a0709;
  }
  html, body {
    margin: 0;
    padding: 0;
    width: 1200px;
    height: 960px;
    overflow: hidden;
    background: var(--paper);
  }
  .sheet {
    display: block;
    width: 1200px;
    height: 960px;
  }
  .dimension-line { stroke: var(--ink); stroke-width: 3; }
  .dimension-label {
    font-family: "Source Sans 3", "Myriad Pro", sans-serif;
    font-size: 21px;
    fill: var(--ink);
  }
  .label-outer { fill: var(--wine-edge); }
  .label-gold { fill: var(--gold); }
  .label-face { fill: url(#wineGlow); }
  .label-rim { fill: none; stroke: var(--rim); stroke-width: 3; opacity: .75; }
  .emblem { fill: var(--emblem); }
  .brand-script {
    font-family: "Parisienne", cursive;
    fill: #ffffff;
  }
  .serif { font-family: "Sorts Mill Goudy", Georgia, serif; }
  .tagline-light { fill: var(--blush); font-size: 21px; }
  .tagline-dark { fill: var(--text-dark); font-size: 31px; }
  .sweet-mark {
    font-family: "Uncial Antiqua", serif;
    font-size: 27px;
    fill: #ffffff;
  }
  .sweet-italic { font-style: italic; fill: #ffffff; font-size: 29px; }
  .detail { fill: var(--cream); }
  .detail-lg { font-size: 25px; }
  .detail-md { font-size: 22px; }
  .detail-sm { font-size: 15px; }
</style>
</head>
<body>
<svg class="sheet" viewBox="0 0 1100 880" xmlns="http://www.w3.org/2000/svg">
  <defs>
    <radialGradient id="wineGlow" cx="50%" cy="50%" r="60%">
      <stop offset="0" stop-color="var(--wine-bright)"/>
      <stop offset="1" stop-color="var(--wine-deep)"/>
    </radialGradient>
    <marker id="arrowHead" viewBox="0 0 10 10" refX="8" refY="5" markerWidth="5" markerHeight="5" orient="auto-start-reverse">
      <path d="M0 0 L10 5 L0 10 Z" fill="var(--ink)"/>
    </marker>
    <filter id="liftShadow" x="-10%" y="-10%" width="120%" height="130%">
      <feDropShadow dx="2" dy="3" stdDeviation="2" flood-color="#3a0008" flood-opacity=".55"/>
    </filter>
    <path id="nutmeadowShape" d="M60 65 Q250 50 440 65 Q472 78 462 132 Q432 232 436 330 Q446 420 474 520 Q484 602 430 630 Q330 646 250 612 Q170 646 70 630 Q16 602 26 520 Q54 420 64 330 Q68 232 38 132 Q28 78 60 65 Z"/>
    <path id="plumvelleShape" d="M622 235 Q815 218 1008 235 Q1046 246 1040 302 Q1000 420 1010 530 Q1046 650 1040 780 Q1030 830 980 828 Q815 814 650 828 Q596 830 590 780 Q584 650 620 530 Q630 420 590 302 Q584 246 622 235 Z"/>
  </defs>

  <!-- Dimension callouts -->
  <g class="dimensions">
    <line class="dimension-line" x1="14" y1="42" x2="478" y2="42" marker-start="url(#arrowHead)" marker-end="url(#arrowHead)"/>
    <text class="dimension-label" x="247" y="35" text-anchor="middle">2.76 inch</text>
    <line class="dimension-line" x1="490" y1="58" x2="490" y2="648" marker-start="url(#arrowHead)" marker-end="url(#arrowHead)"/>
    <text class="dimension-label" transform="translate(500 350) rotate(90)" text-anchor="middle">3.54 inch</text>

    <line class="dimension-line" x1="580" y1="215" x2="1046" y2="215" marker-start="url(#arrowHead)" marker-end="url(#arrowHead)"/>
    <text class="dimension-label" x="813" y="208" text-anchor="middle">2.76 inch</text>
    <line class="dimension-line" x1="1058" y1="228" x2="1058" y2="822" marker-start="url(#arrowHead)" marker-end="url(#arrowHead)"/>
    <text class="dimension-label" transform="translate(1068 525) rotate(90)" text-anchor="middle">3.54 inch</text>
  </g>

  <!-- Nutmeadow label -->
  <g class="label label-nutmeadow">
    <use href="#nutmeadowShape" class="label-outer"/>
    <use href="#nutmeadowShape" class="label-gold" transform="translate(254 346) scale(.955) translate(-250 -346)"/>
    <use href="#nutmeadowShape" class="label-face" transform="translate(252 344) scale(.915 .925) translate(-250 -346)"/>
    <g role="img" aria-label="Crown and berry emblem">
      <ellipse class="emblem" cx="247" cy="197" rx="30" ry="30"/>
    </g>
    <text class="brand-script" x="245" y="298" text-anchor="middle" font-size="86" filter="url(#liftShadow)">Nutmeadow</text>
    <text class="serif tagline-light" x="185" y="352" text-anchor="middle">good mood maker</text>
    <text class="sweet-mark" x="247" y="410" text-anchor="middle">sweet</text>
    <text class="serif detail detail-lg" x="246" y="492" text-anchor="middle">Red Blend</text>
    <text class="serif detail detail-lg" x="246" y="526" text-anchor="middle">California</text>
    <text class="serif detail detail-md" x="246" y="560" text-anchor="middle">2011</text>
    <text class="serif detail detail-sm" x="246" y="582" text-anchor="middle">alc. 12.3%</text>
  </g>

  <!-- Plumvelle label -->
  <g class="label label-plumvelle">
    <use href="#plumvelleShape" class="label-face"/>
    <use href="#plumvelleShape" class="label-rim" transform="translate(815 530) scale(.95 .955) translate(-815 -530)"/>
    <g role="img" aria-label="Crown and berry emblem">
      <ellipse class="emblem" cx="815" cy="286" rx="30" ry="30"/>
    </g>
    <text class="brand-script" x="910" y="432" text-anchor="middle" font-size="42" filter="url(#liftShadow)">Cabernet</text>
    <text class="brand-script" x="815" y="510" text-anchor="middle" font-size="98" filter="url(#liftShadow)">Plumvelle</text>
    <text class="serif tagline-dark" x="820" y="546" text-anchor="middle">good mood wine</text>
    <text class="serif sweet-italic" x="815" y="587" text-anchor="middle">sweet</text>
    <text class="serif detail detail-lg" x="815" y="692" text-anchor="middle">California</text>
    <text class="serif detail detail-md" x="815" y="726" text-anchor="middle">2011</text>
    <text class="serif detail detail-sm" x="815" y="748" text-anchor="middle">alc. 12.3%</text>
  </g>
</svg>
</body>
</html>
```